Child Care Centre needs new roadside billboard / sign*

We have a 2400mm x 1200mm sign that needs to be refreshed. The design is dated and we want to create a new cleaner, more readable roadside signIt needs to be readable from about 100m awayThe text requirements are simple, but we need it to have a warm, family feel.We are located in a small beach side community and we have a lot of bright colours in our centre (a lot of blues and yellows)https://www.saltmarshchildcare.com.au/

Target Market(s)

Parents of young children

Industry/Entity Type

Childcare

Colors
fbed22
0355a3

Requirements
Must have
• Readable from c.100m
• Simple, warm design
Should not have
• Cluttered or overly busy

```html
<!DOCTYPE html>
<html lang="en">
<head>
<meta charset="utf-8">
<title>Saltmarsh Early Education – Roadside Sign</title>
<link rel="stylesheet" href="https://fonts.googleapis.com/css2?family=Itim&family=Open+Sans:wght@700&display=swap">
<style>
  :root {
    --ocean: #0b5a8c;
    --ocean-light: #17699c;
    --sun: #fde24a;
    --sun-deep: #fbed22;
    --ink-blue: #0a4f80;
    --sand: #d8e07c;
    --cloud: #ffffff;
    --rim: #a9a9ad;
    --coral-yellow: #f5d93a;
    --coral-green: #2aa655;
    --page: #fdfdfd;
  }
  * { margin: 0; padding: 0; box-sizing: border-box; }
  html, body {
    width: 1200px; height: 1000px; overflow: hidden;
    background: var(--page);
  }
  .canvas { position: relative; width: 1200px; height: 1000px; }
  .sign {
    position: absolute; left: 66px; top: 56px;
    width: 1067px; height: 534px; overflow: hidden;
    background: var(--ocean);
    border: 1px solid #9fb3c4;
  }
  .sign-backdrop { position: absolute; inset: 0; }
  .brand {
    position: absolute; top: 30px; right: 40px;
    font-family: "Itim", cursive;
    color: var(--ink-blue);
    font-size: 40px; line-height: 1;
    display: flex; align-items: center; gap: 14px;
  }
  .brand-dot {
    width: 40px; height: 40px; border-radius: 50%;
    background: var(--sun-deep);
  }
  .brand-name { display: flex; flex-direction: column; }
  .brand-name span + span { font-size: 32px; margin-top: 6px; }
  .offer-list {
    position: absolute; left: 0; right: 0; top: 184px;
    text-align: center; list-style: none;
    font-family: "Itim", cursive;
    color: var(--sun);
    font-size: 45px; line-height: 54px;
  }
  .phone-bar {
    position: absolute; left: 290px; top: 432px;
    width: 488px; height: 59px;
    background: var(--sun); border-radius: 3px;
    display: flex; align-items: center; justify-content: center; gap: 36px;
    font-family: "Open Sans", sans-serif; font-weight: 700;
    color: var(--ink-blue); font-size: 47px; letter-spacing: -1px;
  }
  .phone-icon { width: 50px; height: 50px; }
  .coral {
    position: absolute; left: 10px; top: 358px;
    width: 112px; height: 140px;
    background: linear-gradient(90deg, var(--coral-yellow) 55%, var(--coral-green) 100%);
    border-radius: 40px 40px 6px 6px;
  }
</style>
</head>
<body>
<div class="canvas">
  <section class="sign">
    <svg class="sign-backdrop" viewBox="0 0 1067 534" width="1067" height="534" aria-hidden="true">
      <path d="M0,20 C250,-20 450,90 1067,40 L1067,110 C500,170 250,60 0,120 Z" fill="var(--ocean-light)"/>
      <path d="M0,200 C300,150 600,250 1067,190 L1067,260 C600,320 300,220 0,270 Z" fill="var(--ocean-light)"/>
      <path d="M0,350 C300,300 650,400 1067,330 L1067,400 C650,470 300,370 0,420 Z" fill="var(--ocean-light)"/>
      <path d="M555,0 C615,8 625,70 645,120 C665,168 730,168 810,158 C900,148 1000,158 1067,146 L1067,0 Z" fill="var(--rim)"/>
      <path d="M555,0 C612,6 620,60 640,108 C660,154 722,156 800,146 C900,136 1000,146 1067,134 L1067,0 Z" fill="var(--cloud)"/>
      <path d="M0,492 C90,478 180,496 220,534 L0,534 Z" fill="var(--sand)"/>
    </svg>

    <div class="brand">
      <span class="brand-dot"></span>
      <div class="brand-name"><span>Saltmarsh</span><span>Early Education</span></div>
    </div>

    <ul class="offer-list">
      <li>6 weeks to 6 years (long day care)</li>
      <li>Open 6.30 am - 6.30 pm - 52 weeks a year</li>
      <li>Before and After School Care</li>
      <li>Vacation Care</li>
    </ul>

    <div class="coral" role="img" aria-label="Cartoon coral growing from the seabed"></div>

    <div class="phone-bar">
      <svg class="phone-icon" viewBox="0 0 50 50" aria-hidden="true">
        <path d="M12,6 l8,9 -5,5 c3,7 8,12 15,15 l5,-5 9,8 -6,7 C20,44 6,30 5,12 Z" fill="var(--ink-blue)"/>
        <path d="M27,10 a13,13 0 0 1 13,13" stroke="var(--ink-blue)" stroke-width="3" fill="none" stroke-linecap="round"/>
        <path d="M27,3 a20,20 0 0 1 20,20" stroke="var(--ink-blue)" stroke-width="3" fill="none" stroke-linecap="round"/>
      </svg>
      <span class="phone-number">07 5550 2846</span>
    </div>
  </section>
</div>
</body>
</html>
```